依頼詳細
新築工事現場にかける会社のイメージシートのデザインをお願い致します。
会社のイメージを高め、会社名と事業内容を知ってもらうことが作成の目的です。

「時代の一歩先を行くハイクオリティでスタイリッシュな上質な空間を創造し、心にゆ
とりを与え、人生を豊かにする住まいを提供する」

会社のミッションは上記となるので
「おしゃれな家を創っている、ハウスビルダー」と
シートを見た方にイメージしてもらえるデザインを希望しています。

写真や文字で細かく表現するよりも、パッと見た時に目をひく、インパクトがあるものが良いと考えています。
家全体を覆うグレイのビニールシートの上に貼る感じなので、そちらも踏まえたカラーリング、デザインをお願いできれば幸いです。
記載項目
ロゴマーク/会社名/キャッチコピー 横1800×縦3600
希望イメージ
シンプル 複雑
単色 カラフル
暗い 明るい
日常 高級
遊び心 厳粛
未来的 伝統的
女性的 男性的
希望する色
黄・オレンジ系、緑系
納品ファイル
• 高解像度JPG (.jpg)
• イラストレーター形式 (.ai)
• フォトショップ形式 (.psd)
• PNG形式 (.png)
補足説明
遠くから見たり、車で走行中に目に入る感じなので、たくさんの文字が入るよりも、できるだけシンプルなものがいいと考えています。
以下の項目は必須で入れていただきたい項目です。

・会社名【株式会社オリベテック】
・検索窓
・ロゴ
・URL【http://olivetec-home.co.jp

宜しくお願い致します。
■ 選んだ理由

シンプルで高級感のあるデザインが気にいりました。

■ 提案者全員のお礼・コメント

皆様、たくさんのご提案ありがとうございました。
素晴らしいご提案がたくさんあり、選出にはとても悩みました。
今後もTadplexさんを活用していくことがあると思いますので、その際はまたお力添えを頂ければ幸いです。

```html
<!DOCTYPE html>
<html lang="ja">
<head>
<meta charset="utf-8">
<title>株式会社オリベテック 現場シート</title>
<link href="https://fonts.googleapis.com/css2?family=Noto+Sans+JP:wght@500;700;900&display=swap" rel="stylesheet">
<style>
  :root {
    --cream: #fcf7e1;
    --edge: #9a9a9a;
    --magenta: #b8237f;
    --pink: #e2416a;
    --orange: #ee8a12;
    --blue: #2b8ccc;
    --green: #3f9b3c;
    --gray: #6a6a6a;
    --dark: #2f2f2f;
    --soft: #8a8a8a;
  }
  html, body { margin: 0; padding: 0; overflow: hidden; }
  body { width: 1200px; height: 2396px; }
  .sheet {
    position: relative;
    width: 1200px; height: 2396px;
    box-sizing: border-box;
    background: var(--cream);
    border: 4px solid var(--edge);
    font-family: "Noto Sans JP", sans-serif;
    overflow: hidden;
  }
  .column {
    position: absolute;
    writing-mode: vertical-rl;
    font-weight: 900;
    line-height: 1;
    white-space: nowrap;
  }
  .column .sm { font-size: 0.6em; font-weight: 700; color: var(--dark); }
  .tagline-lead { left: 900px; top: 80px; font-size: 160px; letter-spacing: -4px; }
  .tagline-main { left: 705px; top: 210px; font-size: 150px; letter-spacing: -4px; }
  .role { left: 490px; top: 260px; font-size: 150px; letter-spacing: -18px; color: var(--green); }
  .company { left: 165px; top: 150px; font-size: 180px; letter-spacing: -10px; color: var(--gray); }
  .c-magenta { color: var(--magenta); }
  .c-pink { color: var(--pink); }
  .c-orange { color: var(--orange); }
  .c-blue { color: var(--blue); }

  .brand {
    position: absolute; left: 0; right: 0; top: 1620px;
    text-align: center; color: var(--gray);
  }
  .brand-name { font-size: 120px; font-weight: 700; letter-spacing: -2px; line-height: 1; }
  .brand-mark { display: inline-block; width: 70px; height: 70px; background: var(--green); margin-right: 24px; vertical-align: 6px; }
  .brand-kana { font-size: 40px; font-weight: 500; letter-spacing: 8px; margin-top: 20px; }

  .search {
    position: absolute; left: 260px; top: 2020px;
    display: flex; height: 84px;
  }
  .search-field {
    width: 560px; box-sizing: border-box;
    border: 4px solid var(--dark); border-radius: 8px 0 0 8px;
    background: #fff; font-size: 50px; font-weight: 500;
    padding-left: 22px; line-height: 76px; color: var(--dark);
  }
  .search-button {
    width: 110px; background: var(--dark); border-radius: 0 8px 8px 0;
    display: flex; align-items: center; justify-content: center;
  }
  .url {
    position: absolute; left: 0; right: 0; top: 2150px;
    text-align: center; font-size: 54px; font-weight: 500; color: var(--dark);
  }
</style>
</head>
<body>
<div class="sheet">
  <div class="column tagline-lead"><span class="c-magenta">時代</span><span class="sm">の</span><span class="c-pink">一歩先</span><span class="sm">を</span><span class="c-magenta">行</span><span class="sm">く</span></div>
  <div class="column tagline-main"><span class="c-orange">上質</span><span class="sm">な</span><span class="c-blue">空間</span><span class="sm">を</span><span class="c-orange">創造</span><span class="sm">する</span></div>
  <div class="column role">ハウスビルダー</div>
  <div class="column company">㈱オリベテック</div>

  <div class="brand">
    <div class="brand-name"><span class="brand-mark"></span>OliveTec</div>
    <div class="brand-kana">オリベテック</div>
  </div>

  <div class="search">
    <div class="search-field">オリベテック</div>
    <div class="search-button">
      <svg width="50" height="50" viewBox="0 0 50 50" aria-hidden="true">
        <circle cx="21" cy="21" r="13" fill="none" stroke="#fff" stroke-width="6"/>
        <line x1="31" y1="31" x2="44" y2="44" stroke="#fff" stroke-width="7" stroke-linecap="round"/>
      </svg>
    </div>
  </div>

  <div class="url">http://olivetec-home.co.jp</div>
</div>
</body>
</html>
```